Wordpress website design for a Herbal Health Care Company

** Outcome of this project is only the design. Only PSD files of the design for unique pages are sufficient.
** There are a number of unique pages in the new site as shown in the wire-frame. However, for the selection of the designer, Homepage, one 2nd tier page (product category) and one 3rd tier page (product page) is sufficient.
We need web design for our for Ayurvedic & Herbal Products Company located in Sri Lanka
Please get the idea about our company by reading the following text
Vision : To be a world class manufacturer and a supplier of highest quality Ayurvedic pharmaceuticals, Herbal health care products, Herbal cosmetics, Essential oils and Oleoresins
Mission : To provide safe and effective Ayurvedic pharmaceuticals, Herbal health care products and Herbal cosmetics, that is of highest quality and integrity, through the incorporation of ancient ayurvedic wisdom with modern technology and scientific management systems for the inprovement of health and longevity of the people.
Policy on Quality : To design, develop, produce and deliver safe, efficacious and consistent quality Herbal health care products based on Ancient Ayurvedic Wisdom using environmentally preferred process technologies and competent personnel towards continual commitment to total customer satisfaction.
(1) Color theme of the website
You can use the color derived from the company logo
(2) Site Map and description of the site
(1) Home
see the wire frame
http://clipvaultia.net/t/kQmRtXwPn4vL
we need drop-down menu for top menu bar
(2) About Vetra Botanics [ This is single page with some description + imaged and following sub page links should be placed in this page]
2.1 Board of Directors
2.2 Milestones
2.3 Our Logo
2.4 Production & R&D
2.5 Certification and Awards
2.6 Global Presence
2.7 Investors
2.8 Distribution
(3)Ayurveda Pharmaceuticals [ This is one of the 3 main categories ,Category Main Page should provide an introduction to the category]
Following shows the sub categories of the “Ayurvedic Pharmaceuticals” . each subcategory has different products. We need unique design for Main Category Page and Sub category
3.1 Arista
3.2 Asava
3.3 Coorna
3.4 Lepa
3.5 Gritha
3.7 Guggulu
3.8 Kalka
3.9 Kwatha
3.10 Pana
see the wireframe
http://clipvaultia.net/t/7NdoGe52KBTT
when you click subcategory , we nee a page like this to list products
http://clipvaultia.net/t/HVrMw3Yq81
(4) Herbal Health Care Products [ This is one of the 3 main categories]
you do not find subcategories, you have only products listed. we need unique design for this category page + products
This page will consists of category description with image and products listed
see the wire frame
(5) Cosmetics & Spa Products
see the wire frame
(6) Essential Oils & Oleoresins
see the wire frame
(7) Media
We need to put video / image gallery / text . and future events
(8) Investors
related information to investors
we need image + text
(9) CSR
(10) Contact US
contact us form / address / telephone number and google map
(11) Log In
Normal login form
(12) Career
Reference Details
http://clipvaultia.net/t/9PcuRN4JWD
http://clipvaultia.net/t/5XkvDMM8Hu
http://clipvaultia.net/t/fQjEyTBoo
Here is a similar site that should give you some idea how we like the new site to look http://www.morvani.com
Industry/Entity Type
Health Care
Requirements
Must have
- We have 4 main categories in our production line
Quality Ayurvedic pharmaceuticals, Herbal health care products, Herbal cosmetics, Essential oils and Oleoresins
You can use 4 boxes below the slider for it ( This very important to have unique different design for each category with some heading, text and images etc)
Nice to have
- You can suggest any good nice features. Try to keep a clean, natural, relaxing theme, with shades of green, white and orange as per their logo. This can be seen from the project brief attachments. www.morvani.com is an example.
Should not have
- Please avoid dark colours (red) and sad colours (grey, black)

```html
<!DOCTYPE html>
<html lang="en">
<head>
<meta charset="utf-8">
<title>Vetra Botanics – A Healthy Long Life</title>
<link href="https://fonts.googleapis.com/css2?family=Arimo:ital,wght@0,400;0,700;1,700&display=swap" rel="stylesheet">
<style>
:root{
  --green-dark:#2f7a14;
  --green:#3f9a1f;
  --green-light:#8cc63f;
  --green-pale:#f3f8ec;
  --orange:#f39a1e;
  --text:#555;
  --muted:#999;
  --line:#dcdcdc;
  --page:#f1f1f1;
  --white:#fff;
}
*{box-sizing:border-box;margin:0;padding:0}
html,body{width:783px;height:1200px;overflow:hidden}
body{position:relative;background:var(--page);font-family:"Arimo",Arial,sans-serif;color:var(--text);font-size:9px;line-height:1.45}
.abs{position:absolute}

/* header */
.site-header{left:0;top:0;width:783px;height:92px;background:linear-gradient(180deg,#4aa524 0%,#2f7a14 70%,#3b8d1a 100%)}
.brand{left:22px;top:14px;display:flex;align-items:center;gap:6px;color:var(--white);font-weight:700;font-size:17px}
.brand-dot{width:14px;height:14px;border-radius:50%;background:var(--white)}
.tagline{left:112px;top:38px;color:var(--white);font-style:italic;font-weight:700;font-size:15px}
.top-links{right:18px;top:10px;display:flex;gap:12px;color:var(--white);font-size:9px;font-weight:700}

/* nav */
.main-nav{left:0;top:92px;width:783px;height:50px;background:var(--white);border-bottom:1px solid var(--line)}
.nav-visual-left{left:14px;top:96px;width:58px;height:40px;border-radius:4px;background:linear-gradient(135deg,#e4eed8,#b9d39c)}
.nav-visual-right{left:668px;top:98px;width:100px;height:80px;border-radius:6px;background:linear-gradient(135deg,#6b6450,#4a4535 55%,#7a7058)}
.nav-items{left:170px;top:100px;display:flex;gap:18px;font-size:9px;color:#333}
.nav-item{line-height:1.2}
.nav-item small{display:block;font-size:7px;color:var(--muted)}
.nav-item.active{color:#c0392b;border-bottom:2px solid var(--orange);padding-bottom:3px}

/* slider */
.slider{left:130px;top:150px;width:525px;height:180px;border:4px solid var(--white);box-shadow:0 1px 3px rgba(0,0,0,.2);background:linear-gradient(100deg,#c9dde6 0%,#e8d2bf 45%,#f0c8a4 60%,#9cbf5a 100%)}
.dots{display:flex;gap:4px}
.dots span{width:6px;height:6px;border-radius:50%;background:#ccc}
.dots span.on{background:var(--orange)}
.slider-dots{left:375px;top:318px}

/* products */
.products{left:130px;top:342px;width:525px;height:208px;background:var(--white);border:1px solid var(--line)}
.panel-title{font-size:10px;color:#444;padding:8px 14px;border-bottom:1px solid var(--line)}
.product-img{top:44px;width:100px;height:110px;border-radius:6px}
.p1{left:34px;background:linear-gradient(160deg,#d9ccae,#9c8a64)}
.p2{left:212px;background:linear-gradient(160deg,#b8d08c,#5f8f30)}
.p3{left:390px;background:linear-gradient(160deg,#9cc37e,#3d7a2a)}
.pager{right:12px;bottom:10px;display:flex;gap:3px}
.pager span{width:9px;height:9px;background:#ccc}
.pager span.on{background:var(--green)}

.divider-mark{left:130px;top:558px;width:8px;height:8px;border-radius:50%;border:1px solid var(--muted)}

/* about */
.about{left:130px;top:575px;width:342px;height:283px;background:var(--green-pale);border:1px solid #d6e6c2;padding:12px 14px}
.about-head{display:flex;gap:8px;align-items:center;margin-bottom:10px}
.about-icon{width:22px;height:22px;background:var(--green-light);border-radius:3px}
.about h2{font-size:12px;font-weight:400;color:#333}
.about .byline{font-size:7px;color:var(--muted)}
.about p{font-size:7.5px;margin-bottom:8px;text-align:justify}

/* side */
.testimonial{left:484px;top:575px;width:171px;height:92px;background:var(--white);border:1px solid var(--line)}
.testimonial-head{background:var(--orange);color:var(--white);font-size:9px;padding:4px 8px}
.testimonial p{padding:8px 10px 2px 22px;font-style:italic;font-size:8px;color:#777}
.testimonial .who{text-align:right;padding-right:10px;font-size:7px;color:var(--muted)}
.tweets{left:484px;top:677px;width:171px;height:180px}
.tweets h3{font-size:10px;font-weight:400;color:#333;padding-left:14px;margin-bottom:8px}
.tweet{background:var(--white);border:1px solid var(--line);padding:6px 8px;font-size:7px;margin-bottom:8px}
.tweet a{color:var(--green);font-weight:700;text-decoration:none}
.tweet .view{display:block;text-align:right;color:var(--orange)}

/* showcase */
.showcase{left:130px;top:870px;width:525px;height:135px}
.show-map{left:6px;top:30px;width:80px;height:70px;border:1px solid var(--line);background:linear-gradient(135deg,#eef2e4,#d4dec6)}
.show-main{left:165px;top:0;width:170px;height:120px;background:linear-gradient(160deg,#f4e7b8,#e2b35a 50%,#7aa83f);border:1px solid var(--line)}
.show-caption{left:165px;top:92px;width:170px;height:28px;background:rgba(20,20,20,.75);color:var(--white);font-size:8px;font-weight:700;padding:4px 8px}
.show-caption small{display:block;font-weight:400;font-size:6px}
.show-jar{left:390px;top:30px;width:58px;height:64px;border:1px solid var(--line);border-radius:4px;background:linear-gradient(180deg,#fbfcf8,#dfe6d6)}
.arrow{top:52px;width:10px;height:14px;color:var(--muted);font-size:12px}

/* footer */
.site-footer{left:0;top:1050px;width:783px;height:150px;background:linear-gradient(180deg,#3f9a1f,#2a6d10)}
.foot-col{top:1060px;color:var(--white);font-size:8px}
.foot-col h4{font-size:10px;font-weight:400;border-bottom:1px solid rgba(255,255,255,.35);padding-bottom:4px;margin-bottom:8px}
.social{display:flex;gap:4px}
.social span{width:12px;height:12px;background:var(--white);border-radius:2px}
.feed a{display:block;color:#ffd27a;font-size:7px;text-decoration:none}
.copyright{left:0;top:1176px;width:783px;text-align:center;color:#dfeed3;font-size:6.5px}
</style>
</head>
<body>

<header class="abs site-header" role="img" aria-label="Green grass header band"></header>
<div class="abs brand"><span class="brand-dot"></span>Vetra Botanics</div>
<div class="abs tagline">" .. A Healthy Long Life "</div>
<nav class="abs top-links"><span>Media</span><span>Investors</span><span>Careers</span><span>CSR</span><span>Contact Us</span><span>Log In</span></nav>

<div class="abs main-nav"></div>
<div class="abs nav-visual-left" role="img" aria-label="Herbal tea cup photograph"></div>
<div class="abs nav-visual-right" role="img" aria-label="Dried tea leaves photograph"></div>
<nav class="abs nav-items">
  <div class="nav-item active">Home</div>
  <div class="nav-item">About Vetra Botanics</div>
  <div class="nav-item">Ayurvedic<small>Pharmaceuticals</small></div>
  <div class="nav-item">Herbal Health<small>Care Products</small></div>
  <div class="nav-item">Cosmetics, Aroma<small>&amp; Spa Products</small></div>
  <div class="nav-item">Essential Oils<small>&amp; Oleoresins</small></div>
</nav>

<div class="abs slider" role="img" aria-label="Woman relaxing in a sunlit green field"></div>
<div class="abs dots slider-dots"><span class="on"></span><span></span><span></span><span></span></div>

<section class="abs products">
  <div class="panel-title">Vetra Botanics Products</div>
  <div class="abs product-img p1" role="img" aria-label="Mortar and pestle with herbs"></div>
  <div class="abs product-img p2" role="img" aria-label="Bundle of fresh herbs"></div>
  <div class="abs product-img p3" role="img" aria-label="Fresh green basil leaves"></div>
  <div class="abs pager"><span class="on"></span><span></span></div>
</section>

<div class="abs divider-mark"></div>

<section class="abs about">
  <div class="about-head"><span class="about-icon"></span><div><h2>About Vetra Botanics</h2><div class="byline">Written by Administrator</div></div></div>
  <p>We blend ancient Ayurvedic wisdom with modern science to create safe, pure and effective herbal products. Every formula begins with carefully chosen plants grown in rich Sri Lankan soil, harvested at the right season and processed with care so that their natural strength reaches you intact. Our teams test each batch for quality, purity and consistency, and our facilities follow strict standards from the field to the finished pack.</p>
  <p>From traditional pharmaceuticals to herbal health care, natural cosmetics and essential oils, our range supports a balanced and healthy way of life. We work closely with farmers and local communities, choose environmentally preferred processes, and invest in research that brings new remedies to families at home and abroad. Our aim is simple: natural care you can trust for a healthy long life.</p>
  <p>Discover our story, our people and the heritage behind every product we make.</p>
</section>

<aside class="abs testimonial">
  <div class="testimonial-head">Testimonials</div>
  <p>Natural, gentle and trusted products that truly make a difference every day.</p>
  <div class="who">— A Happy Customer</div>
</aside>

<aside class="abs tweets">
  <h3>Latest Tweets From Vetra</h3>
  <div class="tweet">New herbal range now available, visit <a>http://vetrabotanics.com</a> to learn more about it.<span class="view">View »</span></div>
  <div class="tweet">Join our wellness day this month, details at <a>http://vetrabotanics.com</a> for all visitors.<span class="view">View »</span></div>
</aside>

<section class="abs showcase">
  <span class="abs arrow" style="left:-10px">‹</span>
  <div class="abs show-map" role="img" aria-label="Regional location map"></div>
  <div class="abs show-main" role="img" aria-label="Range of herbal product packs"></div>
  <div class="abs show-caption">TESTING<small>Quality check</small></div>
  <div class="abs show-jar" role="img" aria-label="Herbal balm jar"></div>
  <span class="abs arrow" style="left:520px">›</span>
</section>

<footer class="abs site-footer"></footer>
<div class="abs foot-col" style="left:60px;width:170px">
  <h4>Follow Us</h4>
  <div class="social"><span></span><span></span></div>
</div>
<div class="abs foot-col feed" style="left:300px;width:180px">
  <h4>Vetra Blog Feeds</h4>
  <a>Herbal care for busy days</a>
  <a>Oils that calm the mind</a>
  <a>Seasonal wellness tips</a>
</div>
<div class="abs foot-col" style="left:540px;width:190px">
  <h4>Our Contact Details</h4>
  <div>E-mail : info@vetrabotanics.com</div>
  <div>Telephone : +94 11 555 0147</div>
  <div>Fax : +94 11 555 0148</div>
</div>
<div class="abs copyright">Vetra Botanics © 2013. All rights reserved.</div>

</body>
</html>
```